Business Card Design

I need a good card to sell my talents in the music field and get my name known as a musician/Guitarist

Industry/Entity Type

Business

Contact Information for Business Card

Leonard Vasquez Musician/Guitarist

```html
<!DOCTYPE html>
<html lang="en">
<head>
<meta charset="utf-8">
<title>Leonard Vasquez – Business Card</title>
<link rel="stylesheet" href="https://fonts.googleapis.com/css2?family=Open+Sans:wght@400;600&display=swap">
<style>
  :root {
    --page: #e9e6e2;
    --card-dark: #0d0806;
    --band-dark: #140c08;
    --wood-glow: #c47020;
    --wood-mid: #8a4614;
    --wood-deep: #3a1a08;
    --text-light: #ffffff;
    --text-soft: #e8e2dc;
    --rule: rgba(255, 255, 255, 0.75);
  }
  * { margin: 0; padding: 0; box-sizing: border-box; }
  html, body {
    width: 1200px; height: 1200px; overflow: hidden;
    background: var(--page);
    font-family: "Open Sans", sans-serif;
  }
  .canvas {
    width: 1200px; height: 1200px;
    display: flex; align-items: center; justify-content: center;
  }
  .business-card {
    position: relative;
    width: 1050px; height: 600px;
    background: var(--card-dark);
    overflow: hidden;
    box-shadow: 0 10px 30px rgba(0,0,0,0.25);
  }
  .guitar-photo {
    position: absolute; left: 0; top: 0; width: 100%; height: 400px;
    background: linear-gradient(100deg, var(--card-dark) 0%, var(--wood-deep) 12%, var(--wood-mid) 32%, var(--wood-glow) 58%, var(--wood-mid) 80%, var(--wood-deep) 100%);
  }
  .contact-band {
    position: absolute; left: 0; top: 400px; width: 100%; height: 200px;
    background: linear-gradient(180deg, #2a150a 0%, var(--band-dark) 35%, var(--card-dark) 100%);
  }
  .name {
    position: absolute; left: 60px; top: 60px;
    font-size: 96px; font-weight: 600; letter-spacing: 1px; line-height: 130px;
    color: var(--text-light);
    text-shadow: 4px 5px 6px rgba(0,0,0,0.75);
    white-space: nowrap;
  }
  .rule { position: absolute; height: 2px; background: var(--rule); }
  .rule-left { left: 30px; top: 262px; width: 380px; }
  .rule-right { left: 690px; top: 208px; width: 330px; }
  .role {
    position: absolute; left: 428px; top: 236px;
    font-size: 34px; line-height: 48px; color: var(--text-soft); letter-spacing: 1px;
    text-shadow: 2px 2px 4px rgba(0,0,0,0.6);
    white-space: nowrap;
  }
  .phone, .address {
    position: absolute; color: var(--text-soft);
    font-size: 26px; line-height: 1.3; letter-spacing: 0.5px;
    display: flex; gap: 14px; align-items: flex-start;
    font-style: normal;
  }
  .phone { left: 200px; top: 452px; align-items: center; }
  .address { left: 570px; top: 432px; }
  .icon { width: 22px; height: 22px; flex: none; fill: var(--text-soft); }
  .address .icon { margin-top: 5px; }
  .divider {
    position: absolute; left: 525px; top: 425px;
    width: 2px; height: 110px; background: var(--rule);
  }
</style>
</head>
<body>
<main class="canvas">
  <section class="business-card">
    <div class="guitar-photo" role="img" aria-label="Photograph of an acoustic guitar in warm amber light"></div>
    <div class="contact-band"></div>

    <h1 class="name">Leonard Vasquez</h1>
    <span class="rule rule-left"></span>
    <span class="rule rule-right"></span>
    <p class="role">Musician/Guitarist</p>

    <p class="phone">
      <svg class="icon" viewBox="0 0 24 24" aria-hidden="true"><path d="M6.6 10.8a15.1 15.1 0 0 0 6.6 6.6l2.2-2.2a1 1 0 0 1 1-.25 11.4 11.4 0 0 0 3.6.57 1 1 0 0 1 1 1V20a1 1 0 0 1-1 1A17 17 0 0 1 3 4a1 1 0 0 1 1-1h3.5a1 1 0 0 1 1 1c0 1.25.2 2.45.57 3.57a1 1 0 0 1-.25 1z"/></svg>
      555-318-2740
    </p>
    <span class="divider"></span>
    <address class="address">
      <svg class="icon" viewBox="0 0 24 24" aria-hidden="true"><path d="M12 2a7 7 0 0 0-7 7c0 5.25 7 13 7 13s7-7.750 7-13a7 7 0 0 0-7-7zm0 9.5A2.5 2.5 0 1 1 12 6.5a2.5 2.5 0 0 1 0 5z"/></svg>
      <span>42 Alder Brook Road<br>Pine Hollow,<br>New York 10477</span>
    </address>
  </section>
</main>
</body>
</html>
```